Valduro.com needs a Mobile FIRST Site

Valduro.com is an insurance broker based in Panama City, Panama that plans to sell car and motorcycle insurance online.

We need to design a total of 5 pages (two of those are A/B test pages). The site will be responsive and will be programmed in React. We will be using Brisk Widget´s library to code Valduro.com. Keep in mind that we are using Brisk Widget to program the site´s functions, not to create the "look and feel" of the site, that is obviously your job. You can learn more about Brisk Widget here... https://brisk-widget.example/

We have created wireframes for the app. Please follow and keep in mind the instructions in the wireframes. You can change things here and there as long as the core functions and goals stay intact. We have uploaded the wireframes along with the company logo and color.

We are planning to A/B test the site´s home page so we need to design two homepages. You can find homepage A and B in the wireframes provided.

We speak Spanish in Panama but you can design the site in English. We can change the text once we receive the designs.

Target Market(s)

25-45 year olds who own a car or motorcylcle and own a credit card.

Industry/Entity Type

Insurance

Font styles to use
Sans Serif

Requirements
Must have
• Follow the wireframes provided and the logo colors.
Nice to have
• Please look at the Image I´ve uploaded from DeskHaven, use it as reference to create HomePage A.

```html
<!DOCTYPE html>
<html lang="en">
<head>
<meta charset="utf-8">
<title>Valduro.com – Claim Here</title>
<link href="https://fonts.googleapis.com/css2?family=Roboto:ital,wght@0,400;0,500;0,700;1,400&display=swap" rel="stylesheet">
<style>
  :root {
    --purple-deep: #2a1a63;
    --purple-bar: #3a2a80;
    --purple-title: #4a3a9c;
    --green: #8dc63f;
    --text-dark: #222222;
    --text-muted: #555555;
    --card-bg: #efefef;
    --button-bg: #ffffff;
    --button-border: #d6d6d6;
    --page-bg: #ffffff;
  }
  * { box-sizing: border-box; margin: 0; padding: 0; }
  html, body {
    width: 675px; height: 1200px; overflow: hidden;
    background: var(--page-bg);
    font-family: "Roboto", Arial, sans-serif;
  }
  .screen { position: relative; width: 675px; height: 1200px; overflow: hidden; }

  .status-bar {
    height: 36px; background: var(--purple-deep);
    display: flex; justify-content: flex-end; align-items: center;
    gap: 12px; padding-right: 18px; color: #fff; font-size: 22px;
  }
  .app-bar {
    height: 104px; background: var(--purple-bar);
    position: relative; display: flex; align-items: center; justify-content: center;
    box-shadow: 0 3px 6px rgba(0,0,0,.25);
  }
  .menu-icon { position: absolute; left: 40px; top: 38px; }
  .brand-name { color: #fff; font-size: 40px; font-weight: 700; letter-spacing: -0.5px; }

  .intro { text-align: center; padding: 0 38px; }
  .page-title {
    margin-top: 32px; color: var(--purple-title);
    font-size: 42px; font-weight: 700; letter-spacing: 0.5px;
  }
  .page-lead {
    margin-top: 12px; color: var(--text-muted);
    font-size: 20.5px; font-style: italic; line-height: 28px;
  }

  .steps {
    margin: 22px 40px 0; display: flex; align-items: center;
  }
  .step { display: flex; align-items: center; gap: 10px; color: var(--green); font-size: 24px; }
  .step-line { flex: 1; height: 2px; background: var(--green); margin: 0 10px; }

  .policy-card {
    position: absolute; left: 38px; top: 405px; width: 599px; height: 765px;
    background: var(--card-bg); border-radius: 4px;
    padding: 36px 48px 0;
  }
  .policy-title { text-align: center; color: var(--text-dark); font-size: 30px; font-weight: 500; }
  .policy-preview {
    margin-top: 38px; height: 270px; background: var(--purple-deep);
    display: flex; align-items: center; justify-content: center;
  }
  .policy-preview .brand-name { font-size: 44px; }

  .actions { margin-top: 24px; display: flex; flex-direction: column; gap: 20px; }
  .action-button {
    height: 82px; background: var(--button-bg);
    border: 1px solid var(--button-border); border-radius: 3px;
    box-shadow: 0 2px 3px rgba(0,0,0,.15);
    display: flex; align-items: center; justify-content: center; gap: 14px;
    font-size: 28px; color: var(--text-dark); font-family: inherit;
  }
</style>
</head>
<body>
<div class="screen">
  <div class="status-bar">
    <svg width="28" height="22" viewBox="0 0 28 22"><path d="M14 21 L0 5 Q14 -5 28 5 Z" fill="#fff"/></svg>
    <svg width="24" height="22" viewBox="0 0 24 22"><path d="M24 0 V22 H0 Z" fill="#fff"/></svg>
    <svg width="14" height="24" viewBox="0 0 14 24"><rect x="4" y="0" width="6" height="3" fill="#fff"/><rect x="0" y="2" width="14" height="22" rx="1" fill="#fff"/></svg>
    <span>12:30</span>
  </div>

  <header class="app-bar">
    <svg class="menu-icon" width="34" height="26" viewBox="0 0 34 26" aria-label="Menu">
      <rect y="1" width="34" height="4" fill="#fff"/><rect y="11" width="34" height="4" fill="#fff"/><rect y="21" width="34" height="4" fill="#fff"/>
    </svg>
    <span class="brand-name">Valduro.com</span>
  </header>

  <section class="intro">
    <h1 class="page-title">CLAIM HERE</h1>
    <p class="page-lead">Lorem ipsum dolor sit amet consectetur adipiscing ullamd orper ramolestie pharetra eros tiorper ncidunt amet.</p>
  </section>

  <nav class="steps">
    <div class="step">
      <svg width="46" height="46" viewBox="0 0 46 46"><circle cx="23" cy="23" r="21" fill="none" stroke="#8dc63f" stroke-width="2.5"/><path d="M13 24 L20 31 L33 16" fill="none" stroke="#8dc63f" stroke-width="3"/></svg>
      <span>Choose</span>
    </div>
    <div class="step-line"></div>
    <div class="step">
      <svg width="46" height="46" viewBox="0 0 46 46"><circle cx="23" cy="23" r="21" fill="none" stroke="#8dc63f" stroke-width="2.5"/><path d="M13 24 L20 31 L33 16" fill="none" stroke="#8dc63f" stroke-width="3"/></svg>
      <span>Verify</span>
    </div>
    <div class="step-line"></div>
    <div class="step">
      <svg width="46" height="46" viewBox="0 0 46 46"><circle cx="23" cy="23" r="21" fill="none" stroke="#8dc63f" stroke-width="2.5"/><path d="M13 24 L20 31 L33 16" fill="none" stroke="#8dc63f" stroke-width="3"/></svg>
      <span>Pay</span>
    </div>
  </nav>

  <section class="policy-card">
    <h2 class="policy-title">Your Insurance Policy</h2>
    <div class="policy-preview" role="img" aria-label="Insurance policy document preview">
      <span class="brand-name">Valduro.com</span>
    </div>
    <div class="actions">
      <button class="action-button">
        <svg width="32" height="32" viewBox="0 0 32 32" fill="none" stroke="#333" stroke-width="2"><path d="M20 4 H4 V28 H28 V14"/><path d="M14 20 L15 15 L27 3 L31 7 L19 19 Z"/></svg>
        Change Data
      </button>
      <button class="action-button">
        <svg width="36" height="26" viewBox="0 0 36 26" fill="none" stroke="#333" stroke-width="2"><rect x="1" y="1" width="34" height="24"/><path d="M1 1 L18 15 L35 1"/></svg>
        Send it to another email
      </button>
      <button class="action-button">
        <svg width="34" height="34" viewBox="0 0 34 34" fill="none" stroke="#333" stroke-width="2"><path d="M17 2 V24 M9 16 L17 24 L25 16"/><path d="M2 22 V32 H32 V22"/></svg>
        Download
      </button>
    </div>
  </section>
</div>
</body>
</html>
```